Label Design for Food Brand

We want a modern label for our spice blends. We are completely open in which direction, it should be modern and beautiful.

Use for Sample spice mixture: "BBQ Tangio"

Here the Packaging:
https://www.kolm-tiegelhaus.example/media/xlarge/1700_1.jpg
Abmessung: Ø 54 x 67 mm

Food

Food

• Logo, Name of Tangio
• Images of food

```html
<!DOCTYPE html>
<html lang="de">
<head>
<meta charset="utf-8">
<title>Bruschetta Topping – Etiketten</title>
<link href="https://fonts.googleapis.com/css2?family=Mulish:wght@300;400;800;900&display=swap" rel="stylesheet">
<style>
  :root {
    --bg: #ffffff;
    --label: #f4f4f4;
    --ink: #333333;
    --orange: #f5a012;
    --sage: #8aab9c;
    --salmon: #e0907c;
  }
  * { margin: 0; padding: 0; box-sizing: border-box; }
  html, body { width: 1200px; height: 750px; overflow: hidden; background: var(--bg); }
  body { font-family: "Mulish", sans-serif; color: var(--ink); position: relative; }

  .label {
    position: absolute;
    top: 284px;
    width: 316px;
    height: 272px;
    background: var(--label);
    border-top: 10px solid var(--accent);
  }
  .label--orange { left: 86px;  --accent: var(--orange); }
  .label--sage   { left: 447px; --accent: var(--sage); }
  .label--salmon { left: 806px; --accent: var(--salmon); }

  .brand-band {
    position: absolute;
    left: 30px; top: 0;
    width: 42px; height: 246px;
    background: var(--accent);
    display: flex; align-items: flex-end; justify-content: center;
    padding-bottom: 12px;
  }
  .brand-name {
    writing-mode: vertical-rl;
    transform: rotate(180deg);
    font-weight: 800;
    font-size: 25px;
    letter-spacing: 2px;
    color: var(--ink);
    line-height: 1;
  }

  .content { position: absolute; left: 83px; top: 35px; width: 225px; }
  .swiss-mark { display: block; width: 22px; height: 22px; margin-bottom: 8px; }

  .product-title { line-height: 0.9; }
  .product-title .bold { display: block; font-weight: 900; font-size: 41px; letter-spacing: 0.3px; }
  .product-title .light { display: block; font-weight: 300; font-size: 40px; letter-spacing: 0.3px; }

  .tagline { margin-top: 10px; font-size: 12px; line-height: 1.1; letter-spacing: 0.4px; }
  .tagline .thin { font-weight: 300; }
  .tagline b { font-weight: 800; }

  .divider { margin-top: 8px; width: 200px; border-top: 2px solid var(--ink); }
  .facts { display: flex; width: 200px; }
  .fact { flex: 1; text-align: center; font-size: 10.5px; line-height: 1.1; padding-top: 6px; letter-spacing: 0.3px; }
  .fact + .fact { border-left: 2px solid var(--ink); }
  .fact .thin { display: block; font-weight: 300; }
  .fact b { display: block; font-weight: 800; }
</style>
</head>
<body>

<section class="label label--orange">
  <div class="brand-band"><span class="brand-name">MEUNKEL</span></div>
  <div class="content">
    <svg class="swiss-mark" viewBox="0 0 22 22" aria-hidden="true"><rect width="22" height="22" fill="#333"/><path d="M9 4h4v5h5v4h-5v5H9v-5H4V9h5z" fill="#fff"/></svg>
    <h1 class="product-title"><span class="bold">BRUS</span><span class="bold">CHETTA</span><span class="light">TOPPING</span></h1>
    <p class="tagline"><span class="thin">HANDGEMACHT MIT </span><b>ZUTATEN<br>HÖCHSTER QUALITÄT</b></p>
    <div class="divider"></div>
    <div class="facts">
      <p class="fact"><span class="thin">NATÜRLICHE</span><b>ZUTATEN</b></p>
      <p class="fact"><span class="thin">ENTWICKELT</span><b>IN DER SCHWEIZ</b></p>
    </div>
  </div>
</section>

<section class="label label--sage">
  <div class="brand-band"><span class="brand-name">MEUNKEL</span></div>
  <div class="content">
    <svg class="swiss-mark" viewBox="0 0 22 22" aria-hidden="true"><rect width="22" height="22" fill="#333"/><path d="M9 4h4v5h5v4h-5v5H9v-5H4V9h5z" fill="#fff"/></svg>
    <h1 class="product-title"><span class="bold">BRUS</span><span class="bold">CHETTA</span><span class="light">TOPPING</span></h1>
    <p class="tagline"><span class="thin">HANDGEMACHT MIT </span><b>ZUTATEN<br>HÖCHSTER QUALITÄT</b></p>
    <div class="divider"></div>
    <div class="facts">
      <p class="fact"><span class="thin">NATÜRLICHE</span><b>ZUTATEN</b></p>
      <p class="fact"><span class="thin">ENTWICKELT</span><b>IN DER SCHWEIZ</b></p>
    </div>
  </div>
</section>

<section class="label label--salmon">
  <div class="brand-band"><span class="brand-name">MEUNKEL</span></div>
  <div class="content">
    <svg class="swiss-mark" viewBox="0 0 22 22" aria-hidden="true"><rect width="22" height="22" fill="#333"/><path d="M9 4h4v5h5v4h-5v5H9v-5H4V9h5z" fill="#fff"/></svg>
    <h1 class="product-title"><span class="bold">BRUS</span><span class="bold">CHETTA</span><span class="light">TOPPING</span></h1>
    <p class="tagline"><span class="thin">HANDGEMACHT MIT </span><b>ZUTATEN<br>HÖCHSTER QUALITÄT</b></p>
    <div class="divider"></div>
    <div class="facts">
      <p class="fact"><span class="thin">NATÜRLICHE</span><b>ZUTATEN</b></p>
      <p class="fact"><span class="thin">ENTWICKELT</span><b>IN DER SCHWEIZ</b></p>
    </div>
  </div>
</section>

</body>
</html>
```